Letterhead design of KESTREL POWER THRIFT INC.

we are a energy saving company doing the solar screen, radian barrier, attic insulation, double panel windows. Basically i need the design of the letterhead including my company name, business address, phone numbers, fax number and email address. Main thing i need it look like a huge company and look like very high class. thanks !!

Reason: Please send me more new design about my company! Thanks so much!!

Industry/Entity Type

Business

```html
<!DOCTYPE html>
<html lang="en">
<head>
<meta charset="utf-8">
<title>Kestrel Power Thrift Inc. — Letterhead</title>
<link rel="stylesheet" href="https://fonts.googleapis.com/css2?family=Lato:wght@700;900&display=swap">
<style>
  :root {
    --brand-green: #0b7d18;
    --mark-green: #8cc864;
    --footer-band: #cde8c5;
    --paper: #ffffff;
  }
  * { margin: 0; padding: 0; box-sizing: border-box; }
  html, body {
    width: 848px;
    height: 1200px;
    overflow: hidden;
    background: var(--paper);
  }
  .letterhead {
    position: relative;
    width: 848px;
    height: 1200px;
    background: var(--paper);
    font-family: "Lato", "Helvetica Neue", Arial, sans-serif;
    color: var(--brand-green);
  }
  .brand-mark {
    position: absolute;
    left: 370px;
    top: 30px;
    width: 105px;
    height: 105px;
    background: var(--mark-green);
  }
  .company-name {
    position: absolute;
    left: 0;
    right: 0;
    top: 142px;
    text-align: center;
    font-size: 48px;
    font-weight: 900;
    letter-spacing: 0.3px;
    line-height: 1.1;
  }
  .contact-band {
    position: absolute;
    left: 0;
    bottom: 0;
    width: 100%;
    height: 101px;
    background: var(--footer-band);
    display: flex;
    flex-direction: column;
    align-items: center;
    justify-content: center;
    font-size: 18px;
    font-weight: 900;
    line-height: 23px;
    text-align: center;
  }
</style>
</head>
<body>
  <main class="letterhead">
    <header>
      <div class="brand-mark" aria-hidden="true"></div>
      <h1 class="company-name">Kestrel Power Thrift Inc.</h1>
    </header>
    <footer class="contact-band">
      <p class="contact-address">2870 Bellmont Ave Suite #410 Houston, TEXAS 77042</p>
      <p class="contact-phone">Office phone # 832-555-0147 Office Fax # 281-555-0193</p>
      <p class="contact-email">Email: kestrelpowerthrift@example.com</p>
    </footer>
  </main>
</body>
</html>
```